vermalo web design

- Company / Site Description
We are developing a website that will allow anyone in Europe to find in one click, cultural things to do (Exhibition, Museum, Monument, Zoo, Aquarium, Archaeological site…) with friends or family, and to organize the visit (book a ticket / a private visit, book a restaurant nearby…).

Examples
1. You're in London with your girlfriend, it's saturday 10 am, you have two hours to spend and you want to see an exhibition. We provide you in one click all the exhibition matching your location / time and date.

2. You're in Berlin with some friends, it's thursday night you want to go out, but you don't know what to do. We provide you a list of experience, you can select for instance "I want to be on top of the world", and we show you a list of venues matching the selected experience / date / time /location of your request.

- Brand name : Vermalo
- Activity : Cultural Leisure, cultural entertainment

- Target audience
Broad target will be between 20 and 55. Core target will be between 25 and 40. Most likely to live in a city and in Europe.

- Behaviours and preferences
Our user is under time constraint (few minutes to find and choose his visit), idea constraint (is not sure about what to do and see) and money constraint.
He wants to have an easy to use website, not cluttered with information, focussed on added value information. He wants to have a website which is modern, fun and elegant that he will deem as professional and trustworthy.

- Our expectations (Do’s and Don’t)
We want to move away from traditional design. We want some OUT OF THE BOX design. Think of a website design that will look like an app design.
We want to make an awesome / extra ordinary /remember-able design. The design must be so cool, that the user wants to come back to the site. In two words: THINK EXTRAORDINARY.
You can use photos to help the user understand functions. If you use photo, use creative commons license photo.
Avoid black colors

- Functional Requirements
We need Four pages:
1. Home Page (desktop and mobile version): it’s both the homepage and the assistant page. This page will allow the user to find in one click his visit (please refer to the pdf file Assistant home page). The page must be self-explanatory for a first time user.
2. Assistant result page (desktop version): it’s the page that display the results found by the assistant based on the criteria search (please refer to the pdf file mockup - Assistant result page)
3. Site / Event page (desktop version): it’s the page that display each result information (please refer to the pdf file mockup – Event / Site Page)
The pdf files list all the elements include in each page + gives you a mockup of each page (just to put in perspective the element required). You are completely free about the design.
We don’t have the logo yet. Use a dummy logo for your page design.
The selected winner can expect to work with us immediately after the contest and on a on a regular basis later on.

- Technical Requirements
No Flash
For the winner, we will manage the CSS you will just need to provide :
. One PSD file containing all the pages
. Inside the PSD file we want for each page two groups: the first group will embed the desktop design, the second group will embed the responsive mobile design (Home Page only).
In total there should be 4 groups inside the PSD file (3 desktop groups, 1 mobile group).
Each group must contain all the elements specified in the pdf file

Website we like
http://demo.plandorix.example/?theme=Velunt
http://rosabel.quintorhub.example/#home
http://blogsite.fenk.daltoroute.example/2/
http://demo.plandorix.example/?theme=Mosaru
http://www.quarnivo.example/themes/lumbe/
http://gridmarket.example/item/tav-responsive-photography-blog-theme/full_screen_preview/8146027
http://items.zkvortel.example/?product=example
http://uk.harnoway.example

Reason: Due to the request of several designers, we have agreed to add 7 additional days to the contest deadline. Thank you. The vermalo team

Reason: We still need to collect all the votes. Sorry for the delay.

Reason: Hello, We extend the contest deadline, in order to collect all the votes from the poll. We should have everything finalized by sunday. Thank you vermalo team

```html
<!DOCTYPE html>
<html lang="en">
<head>
<meta charset="utf-8">
<title>Vermalo – Mobile Home</title>
<link rel="stylesheet" href="https://fonts.googleapis.com/css2?family=Open+Sans:wght@400;600;700&display=swap">
<style>
  :root {
    --red: #e93a31;
    --red-dark: #d7302a;
    --ink: #333333;
    --ink-soft: #555555;
    --grey-icon: #9a9a9a;
    --paper: #f2f2f1;
    --white: #ffffff;
    --field-bottom: #e9e9e9;
    --line: #d6d6d6;
    --photo-dream-top: #2c5a5c;
    --photo-dream-mid: #c99a55;
    --photo-dream-bottom: #3a2a1c;
    --photo-art-a: #f07e62;
    --photo-art-b: #e6dc4a;
    --photo-art-c: #e9e6de;
  }
  * { box-sizing: border-box; margin: 0; padding: 0; }
  html, body { width: 1200px; height: 2831px; overflow: hidden; }
  body {
    position: relative;
    background: var(--paper);
    font-family: "Open Sans", Arial, sans-serif;
    color: var(--ink);
  }

  /* Header */
  .site-header {
    position: absolute; left: 0; top: 0; width: 1200px; height: 302px;
    background: linear-gradient(#ffffff, #f4f4f4);
  }
  .brand {
    position: absolute; left: 37px; top: 110px;
    font-size: 74px; font-weight: 700; letter-spacing: 1px; line-height: 1;
    color: var(--ink);
  }
  .menu-toggle { position: absolute; left: 1078px; top: 140px; width: 82px; height: 44px; }
  .search-toggle { position: absolute; left: 1098px; top: 208px; width: 48px; height: 48px; }

  /* Search assistant */
  .assistant {
    position: absolute; left: 0; top: 302px; width: 1200px; height: 456px;
    background: var(--red);
  }
  .field {
    position: absolute; width: 433px; height: 171px;
    border-radius: 11px;
    background: linear-gradient(#ffffff 40%, var(--field-bottom));
    box-shadow: 0 3px 6px rgba(0,0,0,0.15);
  }
  .field-label {
    position: absolute; left: 40px; top: 50%; transform: translateY(-50%);
    font-size: 43px; font-weight: 700; color: var(--ink);
  }
  .field-icon { position: absolute; right: 28px; top: 50%; transform: translateY(-50%); }
  .field-date { left: 34px; top: 37px; }
  .field-time { left: 502px; top: 37px; }
  .field-location { left: 34px; top: 242px; }
  .field-want { left: 502px; top: 242px; }
  .go-button {
    position: absolute; left: 966px; top: 134px; width: 188px; height: 188px;
    border-radius: 50%;
    background: linear-gradient(#ffffff 50%, #ececec);
    box-shadow: 0 3px 8px rgba(0,0,0,0.2);
    display: flex; align-items: center; justify-content: center;
    font-size: 68px; font-weight: 700; color: var(--red);
  }

  /* I want badge */
  .want-badge {
    position: absolute; left: 450px; top: 815px; width: 302px; height: 302px;
    border-radius: 50%; background: var(--red);
    display: flex; align-items: center; justify-content: center; text-align: center;
    font-size: 64px; font-weight: 700; line-height: 1.1; color: var(--white);
  }
  .want-close { position: absolute; left: 734px; top: 819px; width: 66px; height: 66px; }

  /* Experience cards */
  .card {
    position: absolute; left: 46px; width: 1105px; height: 659px;
    background: var(--white); border-radius: 8px; overflow: hidden;
    box-shadow: 0 2px 6px rgba(0,0,0,0.12);
  }
  .card-photo { width: 100%; height: 530px; }
  .card-title {
    height: 129px; padding-left: 51px;
    display: flex; align-items: center;
    font-size: 43px; font-weight: 400; color: var(--ink);
  }
  .card-dream { top: 1151px; }
  .card-art { top: 1864px; }
  .photo-dream {
    background: linear-gradient(180deg, var(--photo-dream-top) 0%, #5a7a6a 35%, var(--photo-dream-mid) 62%, #a7602a 78%, var(--photo-dream-bottom) 100%);
  }
  .photo-art {
    background: linear-gradient(110deg, var(--photo-art-a) 0%, var(--photo-art-a) 22%, var(--photo-art-c) 40%, #d8d3c8 60%, var(--photo-art-b) 85%);
  }

  .pager { position: absolute; left: 522px; top: 2571px; width: 142px; height: 62px; }

  /* Footer */
  .site-footer {
    position: absolute; left: 0; top: 2680px; width: 1200px; height: 151px;
    border-top: 5px solid var(--line); background: var(--white);
  }
  .copyright {
    position: absolute; left: 51px; top: 56px;
    font-size: 31px; color: var(--ink-soft);
  }
  .more-toggle {
    position: absolute; left: 995px; top: 50px;
    font-size: 38px; font-weight: 700; color: var(--ink-soft);
    display: flex; align-items: center; gap: 14px;
  }
</style>
</head>
<body>

<header class="site-header">
  <div class="brand">VERMALO</div>
  <svg class="menu-toggle" viewBox="0 0 82 44" aria-label="Menu">
    <rect x="0" y="0" width="82" height="6" fill="#333"/>
    <rect x="0" y="18" width="82" height="6" fill="#333"/>
    <rect x="0" y="36" width="82" height="6" fill="#333"/>
  </svg>
  <svg class="search-toggle" viewBox="0 0 48 48" aria-label="Search">
    <circle cx="20" cy="20" r="14" fill="none" stroke="#333" stroke-width="5"/>
    <line x1="30" y1="30" x2="44" y2="44" stroke="#333" stroke-width="6" stroke-linecap="round"/>
  </svg>
</header>

<section class="assistant">
  <div class="field field-date">
    <span class="field-label">Date</span>
    <svg class="field-icon" width="66" height="72" viewBox="0 0 66 72" aria-hidden="true">
      <rect x="3" y="10" width="60" height="58" rx="5" fill="none" stroke="#999" stroke-width="4"/>
      <rect x="3" y="10" width="60" height="14" fill="#999"/>
      <rect x="14" y="2" width="6" height="14" rx="2" fill="#999"/>
      <rect x="46" y="2" width="6" height="14" rx="2" fill="#999"/>
      <g fill="#999">
        <rect x="11" y="31" width="9" height="8"/><rect x="24" y="31" width="9" height="8"/><rect x="37" y="31" width="9" height="8"/><rect x="50" y="31" width="7" height="8"/>
        <rect x="11" y="43" width="9" height="8"/><rect x="24" y="43" width="9" height="8"/><rect x="37" y="43" width="9" height="8"/><rect x="50" y="43" width="7" height="8"/>
        <rect x="11" y="55" width="9" height="7"/><rect x="24" y="55" width="9" height="7"/><rect x="37" y="55" width="9" height="7"/>
      </g>
    </svg>
  </div>
  <div class="field field-time">
    <span class="field-label">Time</span>
    <svg class="field-icon" width="74" height="74" viewBox="0 0 74 74" aria-hidden="true">
      <circle cx="37" cy="37" r="33" fill="none" stroke="#999" stroke-width="4"/>
      <polyline points="37,15 37,39 54,39" fill="none" stroke="#999" stroke-width="4"/>
    </svg>
  </div>
  <div class="field field-location">
    <span class="field-label">Location</span>
    <svg class="field-icon" width="58" height="80" viewBox="0 0 58 80" aria-hidden="true">
      <path d="M29 2 C13 2 2 14 2 29 C2 46 29 78 29 78 C29 78 56 46 56 29 C56 14 45 2 29 2 Z" fill="#999"/>
      <circle cx="29" cy="28" r="10" fill="#fff"/>
    </svg>
  </div>
  <div class="field field-want">
    <span class="field-label">You Want?</span>
    <svg class="field-icon" width="74" height="74" viewBox="0 0 74 74" aria-hidden="true">
      <circle cx="37" cy="37" r="33" fill="none" stroke="#999" stroke-width="4"/>
      <polyline points="24,38 33,47 51,27" fill="none" stroke="#999" stroke-width="5"/>
    </svg>
  </div>
  <div class="go-button">GO</div>
</section>

<div class="want-badge">I<br>WANT</div>
<svg class="want-close" viewBox="0 0 66 66" aria-label="Close">
  <circle cx="33" cy="33" r="29" fill="#fff" stroke="#aaa" stroke-width="6"/>
  <circle cx="33" cy="33" r="20" fill="#aaa"/>
  <line x1="25" y1="25" x2="41" y2="41" stroke="#fff" stroke-width="5"/>
  <line x1="41" y1="25" x2="25" y2="41" stroke="#fff" stroke-width="5"/>
</svg>

<article class="card card-dream">
  <div class="card-photo photo-dream" role="img" aria-label="Photo of a person sitting alone on a bench watching a sunset sky"></div>
  <div class="card-title">Dream</div>
</article>

<article class="card card-art">
  <div class="card-photo photo-art" role="img" aria-label="Photo of a hand colouring a drawing with a marker beside a decorated cup"></div>
  <div class="card-title">Art</div>
</article>

<svg class="pager" viewBox="0 0 142 62" aria-label="Previous and next">
  <circle cx="31" cy="31" r="31" fill="#e93a31"/>
  <polygon points="20,31 38,20 38,42" fill="#fff"/>
  <circle cx="111" cy="31" r="31" fill="#e93a31"/>
  <polygon points="122,31 104,20 104,42" fill="#fff"/>
</svg>

<footer class="site-footer">
  <p class="copyright">Copyright © 2014 Vermalo.com. All Rights Reserved.</p>
  <div class="more-toggle">PLUS
    <svg width="26" height="20" viewBox="0 0 26 20" aria-hidden="true"><polygon points="0,0 26,0 13,20" fill="#888"/></svg>
  </div>
</footer>

</body>
</html>
```